Surface Protection company needs cards

We are a New Zealand company that will apply nanotechnology coatings on surfaces to prevent growth and spread of bacteria, viruses, mold etc with a sprayer. We deal with large corporates, airlines, hospitals and schools so we are after a new modern, simple and clean look that will have great visual impact.
We a company that is focused on prevention and protection.

Company name, Vela Shield

Subtext, Antimicrobial Surface Protection

Logo, VS

Target Market(s)

Hospitals, Transport agencies, Airlines, Corporate entities

Contact Information for Business Card

Company name, VelaShield
Logo, VS

Garth Ormsby
velashieldnz@postkite.example
+64219302648
www.velashield.example.nz

Requirements
Must have
• Simple clean look.
Nice to have
• We apply nano coatings so try and incorporate this into a theme somehow

```html
<!DOCTYPE html>
<html lang="en">
<head>
<meta charset="utf-8">
<title>Vela Shield — Business Cards</title>
<link rel="stylesheet" href="https://fonts.googleapis.com/css2?family=Montserrat:wght@400;500;700;800&display=swap">
<style>
  :root {
    --bg: #d9dcdc;
    --card: #f4f4f2;
    --blue: #1565d8;
    --green: #7dc242;
    --grey: #6f6f6f;
    --ink: #4a4a4a;
  }
  * { box-sizing: border-box; margin: 0; padding: 0; }
  html, body {
    width: 1200px; height: 852px; overflow: hidden;
    background: var(--bg);
    font-family: "Montserrat", Arial, sans-serif;
  }
  .sheet {
    width: 1200px; height: 852px;
    display: flex; align-items: center; justify-content: center; gap: 50px;
  }
  .card {
    position: relative;
    width: 540px; height: 310px;
    background: var(--card);
    border-bottom: 5px solid var(--blue);
    box-shadow: 0 6px 18px rgba(0,0,0,0.12);
  }
  .brand {
    display: flex; flex-direction: column; align-items: flex-end;
  }
  .brand-name {
    display: flex; align-items: center; gap: 12px;
    font-weight: 800; color: var(--blue);
    font-size: 40px; letter-spacing: 0.5px; line-height: 1;
  }
  .brand-dot {
    width: 22px; height: 22px; border-radius: 50%;
    background: var(--green);
  }
  .brand-tagline {
    margin-top: 8px;
    font-size: 11.5px; font-weight: 500; color: var(--grey);
    letter-spacing: 1px; text-transform: uppercase;
  }
  .card-front .brand {
    position: absolute; right: 34px; top: 118px;
  }
  .card-back .brand {
    position: absolute; left: 50%; top: 50%;
    transform: translate(-50%, -50%);
    align-items: center;
  }
  .card-back .brand-name { font-size: 46px; }
  .card-back .brand-tagline { font-size: 13px; }
  .contact {
    position: absolute; left: 34px; top: 106px;
  }
  .contact-name {
    font-size: 20px; font-weight: 700; color: var(--blue);
  }
  .contact-role {
    font-size: 13px; color: var(--ink); margin: 2px 0 12px;
  }
  .contact-list { list-style: none; }
  .contact-list li {
    display: flex; align-items: center; gap: 9px;
    font-size: 13px; color: var(--ink); margin-bottom: 6px;
  }
  .contact-list svg { width: 13px; height: 13px; flex: none; }
</style>
</head>
<body>
<main class="sheet">
  <section class="card card-front">
    <div class="contact">
      <p class="contact-name">Garth Ormsby</p>
      <p class="contact-role">Director</p>
      <ul class="contact-list">
        <li>
          <svg viewBox="0 0 16 16" aria-hidden="true"><path d="M4 1.5 6.5 4 5 5.8c.9 2 2.5 3.6 4.6 4.6L11.4 9l2.5 2.5-1.6 2.3C7 13.5 2.3 8.8 2 3.2z" fill="var(--blue)"/></svg>
          +64219302648
        </li>
        <li>
          <svg viewBox="0 0 16 16" aria-hidden="true"><rect x="1.5" y="3.5" width="13" height="9" fill="none" stroke="var(--blue)" stroke-width="1.4"/><path d="M1.5 3.5 8 9l6.5-5.5" fill="none" stroke="var(--blue)" stroke-width="1.4"/></svg>
          velashieldnz@postkite.example
        </li>
        <li>
          <svg viewBox="0 0 16 16" aria-hidden="true"><circle cx="8" cy="8" r="6.3" fill="none" stroke="var(--blue)" stroke-width="1.3"/><ellipse cx="8" cy="8" rx="2.8" ry="6.3" fill="none" stroke="var(--blue)" stroke-width="1.1"/><path d="M1.7 8h12.6M2.8 4.8h10.4M2.8 11.2h10.4" stroke="var(--blue)" stroke-width="1.1"/></svg>
          www.velashield.example.nz
        </li>
      </ul>
    </div>
    <div class="brand">
      <p class="brand-name"><span class="brand-dot"></span>Vela Shield</p>
      <p class="brand-tagline">Antimicrobial Surface Protection</p>
    </div>
  </section>

  <section class="card card-back">
    <div class="brand">
      <p class="brand-name"><span class="brand-dot"></span>Vela Shield</p>
      <p class="brand-tagline">Antimicrobial Surface Protection</p>
    </div>
  </section>
</main>
</body>
</html>
```